Avocado Smoothies (100% Natural, No Preservatives, No added Sugar)

We need a company logo (for business cards etc) as well as label design (front and back) for a range of avocado based smoothies on our 300 ml bottle & pouch with drinking spout. The look & feel of the label is that the smoothies are fresh & healthy, prepared with freshest ingredients & formulated with nutritional needs in mind.

The final design should give the impression of a genuine & trusted brand of beverage that is appealing to (1) health conscious busy professionals both male & female (e.g. gym / yoga / athletic buffs), (2) busy mothers of fussy / picky kids; and (3) people who like more plant-based diets, who want the best products for them / their families. The design is to be innovative & appealing to the intelligent health conscious consumers especially avocado fans, looking for healthier alternatives of natural drinks on-the go, that are NOT prepared by big, impersonal & highly automated factories that use all sorts of nasties & processes in their beverages. Easy to read FONT and preferably include an original picture of avocado (which can be a real picture / graphic design) - however, this is not necessary.

Company name: OWRU Pte.Ltd. (the letter "I" may mean "I" or "Innovative" or "Intelligent". "OWRU" can be a play of the word "I ever .... " e.g. "all OWRU wanted is ... ".)

Please note that the master label design should be versatile enough for a range of avocado smoothies (we only need to make minimum changes to the main picture / words as necessary for each specific avocado smoothie) and the label can also be used for kids size and adult size pouches and bottles of height 16cm and diameter of circular base of 5.5cm.

Target Market(s)

(1) health conscious busy professionals (e.g. gym / yoga / athletic buffs), (2) busy mothers of fussy / picky kids; and (3) vegans & people who like more plant based diets, who want the best products for them / their families.

Logo Text

OWRU

Font styles to use
Serif
Sans Serif
Decorative
Script

Colors

Designer to choose colors to be used in the design.

Requirements
Must have
• Centre attention of the label (BIG font): Avocado & [we insert the other main ingredients] Smoothie
• Company logo (noticeable somewhere on the label): OWRU
• (Medium font) All natural ingredients, no added sugar or salt, no additives or preservatives
• (Smaller fonts) Along the lines of: "Made from the finest blend of avocados and [we can insert other ingredients] to nourish you. Rich, creamy, wholesome & unique avocado experience that is good and satisfyingly delicious! "
• Keep refrigerated below 5 deg C
• Manufactured by: [we insert details]
• 300ml
Nice to have
• Please recycle usual logo
• originality & fresh & appealing factor
Should not have
• unhealthy image / junk food / sugary / additives / unsavoury impression
• difficult to read font
• confusion with other existing brands

```html
<!DOCTYPE html>
<html lang="en">
<head>
<meta charset="utf-8">
<title>OWRU Avocado &amp; Strawberry Smoothies – Front Label</title>
<link href="https://fonts.googleapis.com/css2?family=Cormorant+Garamond:wght@400;500&family=Josefin+Sans:wght@400;600&display=swap" rel="stylesheet">
<style>
  :root {
    --backdrop: #d0cbbd;
    --label: #f5f3ef;
    --band: #ecebe6;
    --ink: #1c1a18;
    --berry: #d4362c;
    --berry-deep: #b8241d;
    --leaf: #3f7d2c;
    --avocado-flesh: #e8d77a;
    --avocado-skin: #7fae3a;
    --seed: #6a3a28;
  }
  html, body {
    margin: 0;
    width: 1200px;
    height: 900px;
    overflow: hidden;
    background: var(--backdrop);
  }
  h1, p { margin: 0; }
  .label {
    position: absolute;
    left: 400px;
    top: 120px;
    width: 400px;
    height: 660px;
    background: var(--label);
    overflow: hidden;
    font-family: "Josefin Sans", sans-serif;
    color: var(--ink);
  }
  .brand {
    position: absolute;
    top: 44px;
    left: 0;
    width: 100%;
    text-align: center;
    font-family: "Cormorant Garamond", serif;
    font-weight: 400;
    font-size: 86px;
    letter-spacing: 10px;
    line-height: 1;
    padding-left: 10px;
    box-sizing: border-box;
  }
  .brand sup {
    font-size: 11px;
    letter-spacing: 0;
    vertical-align: top;
    position: relative;
    top: 10px;
  }
  .intro {
    position: absolute;
    top: 150px;
    left: 40px;
    right: 40px;
    text-align: center;
    font-size: 7.5px;
    line-height: 1.35;
  }
  .fruit-art {
    position: absolute;
    top: 176px;
    left: 0;
    width: 100%;
    height: 224px;
    background:
      radial-gradient(ellipse 60% 30% at 50% 22%, var(--leaf) 0 55%, transparent 72%),
      linear-gradient(180deg, transparent 0 38%, var(--berry) 52%, var(--berry-deep) 100%);
  }
  .flavour-band {
    position: absolute;
    top: 400px;
    left: 0;
    width: 100%;
    height: 112px;
    background: var(--band);
    text-align: center;
  }
  .flavour {
    margin-top: 12px;
    font-size: 19px;
    letter-spacing: 2px;
    line-height: 1.1;
  }
  .product {
    margin-top: 6px;
    font-size: 38px;
    font-weight: 600;
    letter-spacing: 2px;
    line-height: 1;
  }
  .underline {
    display: block;
    margin: 3px auto 0;
  }
  .claim {
    margin-top: 6px;
    font-size: 19px;
    letter-spacing: 2px;
    line-height: 1.1;
  }
  .avocado-art {
    position: absolute;
    top: 512px;
    left: 0;
    width: 100%;
    height: 148px;
    background:
      radial-gradient(ellipse 24% 42% at 50% 14%, var(--seed) 0 90%, transparent 100%),
      radial-gradient(ellipse 75% 120% at 50% 10%, var(--avocado-flesh) 0 60%, var(--avocado-skin) 100%);
  }
  .blurb {
    position: absolute;
    bottom: 12px;
    left: 0;
    width: 100%;
    text-align: center;
    font-size: 7.5px;
    line-height: 1.35;
  }
  .badges {
    position: absolute;
    right: 8px;
    top: 544px;
    display: flex;
    flex-direction: column;
    gap: 6px;
    align-items: center;
  }
  .badge {
    display: flex;
    flex-direction: column;
    align-items: center;
    font-size: 5px;
  }
</style>
</head>
<body>
  <main class="label">
    <h1 class="brand">OWRU<sup>TM</sup></h1>
    <p class="intro">Lorem ipsum dolor sit amet, consectetuer adipiscing elit, sed diam nonummy<br>nibh euismod tincidunt ut laoreet dolore magna aliquam erat volutpat.</p>

    <div class="fruit-art" role="img" aria-label="Halved strawberry with green leaves, splashed with milk"></div>

    <section class="flavour-band">
      <p class="flavour">AVOCADO &amp; STRAWBERRY</p>
      <p class="product">SMOOTHIES</p>
      <svg class="underline" width="260" height="4" viewBox="0 0 260 4"><path d="M2 2 L258 2" stroke="#1c1a18" stroke-width="2.5" stroke-linecap="round"/></svg>
      <p class="claim">ALL NATURAL INGREDIENTS</p>
    </section>

    <div class="avocado-art" role="img" aria-label="Halved avocado showing its seed"></div>

    <p class="blurb">Made from the finest<br>blend of avocados and</p>

    <div class="badges">
      <div class="badge"><svg width="22" height="22" viewBox="0 0 22 22"><circle cx="11" cy="11" r="9.5" fill="none" stroke="#1c1a18" stroke-width="1.2"/><line x1="4.5" y1="4.5" x2="17.5" y2="17.5" stroke="#1c1a18" stroke-width="1.2"/></svg>No Sugar</div>
      <div class="badge"><svg width="22" height="22" viewBox="0 0 22 22"><circle cx="11" cy="11" r="9.5" fill="none" stroke="#1c1a18" stroke-width="1.2"/><line x1="4.5" y1="4.5" x2="17.5" y2="17.5" stroke="#1c1a18" stroke-width="1.2"/></svg>No Salt</div>
      <div class="badge"><svg width="22" height="22" viewBox="0 0 22 22"><circle cx="11" cy="11" r="9.5" fill="none" stroke="#1c1a18" stroke-width="1.2"/><line x1="4.5" y1="4.5" x2="17.5" y2="17.5" stroke="#1c1a18" stroke-width="1.2"/></svg>No Preservatives</div>
    </div>
  </main>
</body>
</html>
```